Broschüre für Gleichstellungsstelle einer kommunalen Stadtverwaltung
Sehr schönes und stimmiges Design, super schnelle Bearbeitung und zuvorkommende Kommunikation!
Zielgruppe
Wir sind die Gleichstellungsstelle einer kommunalen Stadtverwaltung (Einwohner*innen ca. 74.500) und richten uns mit unserer Arbeit grundsätzlich an alle Menschen.
Wir wollen eine Broschüre zum Handlungsleitfaden für die geschlechtergerechte Sprache bei der Stadt erstellen. Dieser soll an die Beschäftigten als Unterstützung verteilt werden.
Aufgabenstellung
- Broschüre mit Wire-O-Bindung, Druckformat 14,8 cm x 14,8 cm, Endformat 15,0 x 15,0 cm
- Spiralbindung an der Kopfseite
- doppelseitiges Deckblatt und Rückseite
- 16 Seiten Inhalt, wobei lediglich die Vorderseiten Text enthalten
- Schriftart (optimal Avenir Next, alternativ Arial) und Farbschema laut Corporate Design
- Der Text ist vorgegeben, die Gestaltung ist im Rahmen des Corporate Designs frei
Es soll eine ansprechende Broschüre gestaltet werden, welche die Leser*innen zum Blättern einlädt. Das bedeutet, dass alle Seiten (Deckblatt, Inhaltsseiten und Rückseiten) bei der Gestaltung berücksichtigt werden müssen.
Am Ende soll neben den üblichen Dateien auch eine fertige Druckdatei (siehe Datenblatt) zur Verfügung gestellt werden. Dabei ist zu beachten, dass die Spiralbindung des fertigen Produkts an der Kopfseite sein soll.

```html
<!DOCTYPE html>
<html lang="de">
<head>
<meta charset="utf-8">
<title>Gendersternchen</title>
<link rel="stylesheet" href="https://fonts.googleapis.com/css2?family=Nunito+Sans:wght@400;700;800&display=swap">
<style>
  :root {
    --green-dark: #024e47;
    --sage: #98b3ab;
    --sage-text: #a9c1ba;
    --grey-text: #a6a6a6;
    --white: #ffffff;
  }
  html, body {
    margin: 0;
    padding: 0;
    overflow: hidden;
    background: var(--white);
  }
  .page {
    position: relative;
    width: 1200px;
    height: 1200px;
    overflow: hidden;
    background: var(--white);
    font-family: "Nunito Sans", Arial, sans-serif;
    color: var(--white);
  }
  .intro {
    position: absolute;
    left: 0; top: 0;
    width: 1200px; height: 380px;
    background: var(--green-dark);
    box-sizing: border-box;
    padding: 72px 0 0 81px;
  }
  .intro h1 {
    margin: 0;
    font-size: 34px;
    font-weight: 800;
    letter-spacing: 0.5px;
    line-height: 40px;
  }
  .intro p {
    margin: 0;
    font-size: 28px;
    line-height: 41.5px;
    font-weight: 400;
  }
  .intro .accent { color: var(--sage-text); font-weight: 700; }

  .example {
    position: absolute;
    height: 74px;
    background: var(--sage);
    box-sizing: border-box;
    padding-left: 16px;
    font-size: 33px;
    font-weight: 700;
    line-height: 74px;
    white-space: nowrap;
  }
  .ex-1 { left: 64px;  top: 422px; width: 451px; }
  .ex-2 { left: 592px; top: 422px; width: 449px; padding-left: 28px; }
  .ex-3 { left: 64px;  top: 507px; width: 451px; }
  .ex-4 { left: 592px; top: 507px; width: 449px; padding-left: 28px; }

  .tip {
    position: absolute;
    left: 0; top: 634px;
    width: 919px; height: 215px;
    background: var(--green-dark);
  }
  .tip-mark { position: absolute; left: 44px; top: 28px; }
  .tip-text {
    position: absolute;
    left: 122px; top: 22px;
  }
  .tip-text h2 {
    margin: 0;
    font-size: 30px;
    font-weight: 800;
    line-height: 40px;
  }
  .tip-text p {
    margin: 0;
    font-size: 27px;
    line-height: 43px;
  }

  .speech-note {
    position: absolute;
    left: 81px; top: 883px;
    margin: 0;
    font-size: 26px;
    line-height: 35px;
    color: var(--grey-text);
  }
  .speech-example {
    position: absolute;
    left: 275px; top: 1036px;
    width: 631px; height: 73px;
    background: var(--sage);
    font-size: 34px;
    font-weight: 700;
    line-height: 73px;
    text-align: center;
    white-space: nowrap;
  }
</style>
</head>
<body>
<main class="page">
  <section class="intro">
    <h1>GENDERSTERNCHEN</h1>
    <p>Das Gendersternchen dient als <span class="accent">sprachliches Darstellungsmittel</span><br>
    aller Geschlechter und Geschlechtsidentitäten:<br>
    Im Schriftlichen wird das Sternchen (*) zwischen die maskuline und<br>
    feminine Endung eines Wortes eingesetzt, auch bei Artikeln und<br>
    Pronomen. Zum Beispiel:</p>
  </section>

  <div class="example ex-1">der*die Mitarbeiter*in</div>
  <div class="example ex-2">die Mitarbeiter*innen</div>
  <div class="example ex-3">ein*e Mitarbeiter*in</div>
  <div class="example ex-4">jede*r Mitarbeiter*in</div>

  <aside class="tip">
    <svg class="tip-mark" width="50" height="170" viewBox="0 0 50 170" aria-hidden="true">
      <rect x="3" y="1" width="44" height="102" fill="#ffffff"/>
      <circle cx="25" cy="147" r="22" fill="#ffffff"/>
    </svg>
    <div class="tip-text">
      <h2>TIPP:</h2>
      <p>Greifen Sie nach Möglichkeit bei der Formulierung<br>
      mit Gendersternchen auf die Pluralform zurück, dabei<br>
      muss der Artikel in der Regel nicht gegendert werden.</p>
    </div>
  </aside>

  <p class="speech-note">Das Gendersternchen (*) wird mit einer kurzen stimmlosen Pause ge-<br>
  sprochen, auch Verschlusslaut, glottaler Schlag oder kurz Glottisschlag<br>
  genannt. Zum Beispiel:</p>

  <div class="speech-example">Mitarbeiter [kurze Pause] innen</div>
</main>
</body>
</html>
```